Biz Cards to match new logo

I'm looking for a business card layout to go with my new logo. I'd like to have one side in colour (purple, with the logo in white) and the other side to be white with the purple logo and contact info in black font: name, address (2 lines), phone, email, fax, website. The logo includes the company name so it doesn't need to be repeated in the text. The font should be legibile to the semi-blind. (I hate small fonts on business cards).

Industry/Entity Type

Business

```html
<!DOCTYPE html>
<html lang="en">
<head>
<meta charset="utf-8">
<title>Vesta Research – Business Cards</title>
<link href="https://fonts.googleapis.com/css2?family=Open+Sans:wght@400;600&display=swap" rel="stylesheet">
<style>
  :root {
    --purple: #5f3a8c;
    --purple-deep: #56327f;
    --paper: #f7f7f5;
    --ink: #111111;
    --shade: #b4b4b4;
    --backdrop: #3b3b3b;
  }
  * { margin: 0; padding: 0; box-sizing: border-box; }
  html, body {
    width: 1200px;
    height: 1200px;
    overflow: hidden;
    background: var(--backdrop);
    font-family: "Open Sans", Arial, sans-serif;
  }
  .sheet {
    width: 1200px;
    height: 1200px;
    display: flex;
    flex-direction: column;
    align-items: center;
    justify-content: center;
    gap: 60px;
  }
  .card {
    position: relative;
    width: 840px;
    height: 480px;
    overflow: hidden;
    box-shadow: 0 12px 30px rgba(0,0,0,0.35);
  }

  /* Front: colour side */
  .card-front {
    background: linear-gradient(135deg, var(--purple) 0%, var(--purple-deep) 100%);
  }
  .card-front .brand {
    position: absolute;
    left: 50%;
    top: 50%;
    transform: translate(-50%, -50%);
    display: flex;
    align-items: center;
    gap: 18px;
    color: #ffffff;
    font-weight: 600;
    font-size: 52px;
    letter-spacing: 2px;
    white-space: nowrap;
  }
  .brand-mark {
    width: 26px;
    height: 26px;
    background: currentColor;
  }

  /* Back: white contact side */
  .card-back { background: var(--paper); }
  .accent-bar {
    position: absolute;
    background: var(--purple);
  }
  .accent-shade {
    position: absolute;
    background: var(--shade);
  }
  .accent-bar.left  { left: 0;    top: 176px; width: 96px;  height: 62px; }
  .accent-shade.left{ left: 96px; top: 176px; width: 14px;  height: 62px; }
  .accent-bar.right { right: 0;   top: 300px; width: 126px; height: 70px; }
  .accent-shade.right{ right: 126px; top: 300px; width: 14px; height: 70px; }

  .card-back .brand {
    position: absolute;
    left: 150px;
    top: 190px;
    color: var(--purple);
    font-weight: 600;
    font-size: 34px;
    letter-spacing: 1px;
    white-space: nowrap;
  }
  .divider {
    position: absolute;
    left: 440px;
    top: 120px;
    width: 2px;
    height: 250px;
    background: var(--purple);
  }
  .contact {
    position: absolute;
    left: 468px;
    top: 122px;
    list-style: none;
    font-size: 25px;
    line-height: 33px;
    color: var(--ink);
  }
  .contact .name {
    color: var(--purple);
    margin-bottom: 14px;
  }
</style>
</head>
<body>
  <main class="sheet">
    <section class="card card-front" aria-label="Card front">
      <div class="brand"><span class="brand-mark"></span>Vesta Research</div>
    </section>

    <section class="card card-back" aria-label="Card back">
      <div class="accent-bar left"></div>
      <div class="accent-shade left"></div>
      <div class="brand">Vesta Research</div>
      <div class="divider"></div>
      <ul class="contact">
        <li class="name">Name</li>
        <li>Address line 1</li>
        <li>Address line 2</li>
        <li>Phone</li>
        <li>Email</li>
        <li>Fax</li>
        <li>website</li>
      </ul>
      <div class="accent-shade right"></div>
      <div class="accent-bar right"></div>
    </section>
  </main>
</body>
</html>
```